Investment website design - investing in mutual funds

I need a design of a website (only homepage for now) dedicated to investment in mutual funds. Attached is a mock up with all the elements the homepage design should contain. The homepage should contain a logo in the upper left corner, the domain the website will run on is www.perovalstrinka.cz , in the upper right corner there should be 2 buttons or links SIGN UP / SIGN IN. The bottom of the homepage should contain links to ABOUT US, FAQ, PRIVACY POLICY, CONTACT US.
Now the main elements on the homepage
1) Video that will explain how the investment works exactly, under this video we will have 3 illustrated icons like the ones attached (see 2nd attachement) that will show the potential investor what exactly they could get when investing with us (education for kids, happy life after they retire, regular monthly payment for the rest of their life).
2) On the right side next to the video we will have a calculator where a potential investor can play with the numbers, the investor can fill in the MONTHLY PAYMENT that he wants to invest regularly every month, the time frame of the investment - for how long he wants to invest. Once the potential investor selects those 2 variables we will calculate for him 2 options - either he can get a ONE TIME PAYOUT once he reaches his investment horizon or he can get a regular monthly payment for the rest of his life. Under the laculator there will be a button 'I want to invest ->'. The functionality of the calculator should be similar to the calculator that can be found here http://www.brodavbank.cz/brodav-podilove-fondy/ and https://felbo.cz/.
The design should look similar to https://felbo.cz/ (font, colors, logo). We prefer white background in the area where we have the video and calculator. We also like the design of www.tarvupo.com. Let me know if you have any questions.

```html
<!DOCTYPE html>
<html lang="en">
<head>
<meta charset="utf-8">
<title>Perovalstrinka – Mutual Fund Investing</title>
<link rel="stylesheet" href="https://fonts.googleapis.com/css2?family=Roboto:wght@400;500;700&family=Varela+Round&display=swap">
<style>
  :root {
    --teal: #43b2bf;
    --teal-dark: #3aa2ae;
    --red: #e9573b;
    --white: #ffffff;
    --light-grey: #f2f2f2;
    --laptop: #ececec;
    --text-dark: #4a4a4a;
    --track: #3f3f3f;
  }
  * { box-sizing: border-box; margin: 0; padding: 0; }
  html, body { width: 1200px; height: 710px; overflow: hidden; }
  body {
    position: relative;
    background: var(--teal);
    font-family: "Roboto", Arial, sans-serif;
    color: var(--white);
  }

  .brand {
    position: absolute; left: 88px; top: 16px;
    font-weight: 700; font-size: 32px; letter-spacing: -0.5px;
    color: var(--white);
  }
  .account-nav { position: absolute; top: 19px; left: 896px; display: flex; gap: 8px; }
  .btn {
    display: flex; align-items: center; justify-content: center;
    width: 104px; height: 34px; font-size: 16px; text-decoration: none;
  }
  .btn-signin { background: var(--red); color: var(--white); }
  .btn-signup { width: 103px; background: var(--light-grey); color: var(--text-dark); border: 1px solid #ddd; }

  .video-screen {
    position: absolute; left: 110px; top: 102px; width: 528px; height: 358px;
    background: var(--laptop); border-radius: 12px 12px 0 0; padding: 24px 25px 20px;
  }
  .video-frame {
    width: 100%; height: 100%;
    background: linear-gradient(135deg, #fdfdfd 0%, #f7f1ea 45%, #f2c4a8 60%, #fbfbfb 100%);
  }
  .laptop-base {
    position: absolute; left: 50px; top: 458px; width: 648px; height: 12px;
    background: #f3f3f3; border-radius: 0 0 40% 40% / 0 0 100% 100%;
  }
  .laptop-shadow {
    position: absolute; left: 70px; top: 470px; width: 608px; height: 22px;
    background: linear-gradient(180deg, rgba(255,255,255,0.45), rgba(255,255,255,0));
  }

  .benefit {
    position: absolute; top: 503px; width: 160px;
    text-align: center; font-size: 14.4px; list-style: none;
  }
  .benefit:nth-child(1) { left: 158px; }
  .benefit:nth-child(2) { left: 295px; }
  .benefit:nth-child(3) { left: 437px; }
  .benefit-icon {
    width: 75px; height: 75px; border-radius: 50%; margin: 0 auto 6px;
    background: radial-gradient(circle, #f6b84a 0%, #f2a24b 30%, #ffffff 62%);
  }

  .calculator h1 {
    position: absolute; left: 686px; top: 128px; line-height: 1;
    font-family: "Varela Round", Arial, sans-serif;
    font-size: 37px; font-weight: 400; white-space: nowrap;
    -webkit-text-stroke: 1px var(--white);
  }
  .field {
    position: absolute; left: 689px; width: 422px; height: 45px;
    border: none; background: var(--white); padding: 0 12px;
    font-family: inherit; font-size: 13.5px; color: var(--text-dark);
  }
  .field::placeholder { color: var(--text-dark); }
  .field-investment { top: 186px; }
  .field-payout { top: 305px; height: 49px; }
  .field-monthly { top: 378px; height: 50px; }
  .length-label { position: absolute; left: 700px; top: 240px; font-size: 13.5px; font-weight: 500; }
  .slider { position: absolute; left: 690px; top: 274px; width: 410px; height: 5px; background: var(--track); border-radius: 3px; }
  .slider-fill { position: absolute; left: 0; top: 0; width: 30px; height: 5px; background: var(--red); border-radius: 3px 0 0 3px; }
  .slider-thumb { position: absolute; left: 24px; top: -6px; width: 12px; height: 17px; background: #f4f4f4; border-radius: 2px; }
  .slider-scale {
    position: absolute; left: 692px; top: 282px; width: 408px;
    display: flex; justify-content: space-between; font-size: 13px; font-weight: 500;
  }
  .or { position: absolute; left: 689px; top: 359px; width: 422px; text-align: center; font-size: 13px; font-weight: 500; }
  .btn-invest {
    position: absolute; left: 936px; top: 441px;
    display: flex; align-items: center; justify-content: center;
    width: 175px; height: 38px;
    background: var(--red); color: var(--white); text-decoration: none;
    font-weight: 700; font-size: 14.5px;
  }

  .site-footer {
    position: absolute; left: 0; right: 0; top: 644px; height: 66px;
    border-top: 1px solid var(--teal-dark);
    display: flex; justify-content: center; align-items: center; padding-bottom: 2px;
    font-size: 12px;
  }
  .site-footer a { color: var(--white); text-decoration: none; }
  .site-footer span { margin: 0 8px; }
</style>
</head>
<body>
  <header>
    <div class="brand">Perovalstrinka</div>
    <nav class="account-nav">
      <a class="btn btn-signin" href="#">SIGN IN</a>
      <a class="btn btn-signup" href="#">SIGN UP</a>
    </nav>
  </header>

  <main>
    <div class="video-screen">
      <div class="video-frame" role="img" aria-label="Explainer video: cheerful businessman beside a play button and a money tree with gold coins"></div>
    </div>
    <div class="laptop-base"></div>
    <div class="laptop-shadow"></div>

    <ul class="benefits">
      <li class="benefit"><div class="benefit-icon" role="img" aria-label="Stack of books with a graduation cap"></div>Education for kids</li>
      <li class="benefit"><div class="benefit-icon" role="img" aria-label="Person relaxing in a bean bag"></div>Passive income</li>
      <li class="benefit"><div class="benefit-icon" role="img" aria-label="Retiree playing golf"></div>Happy retirement</li>
    </ul>

    <section class="calculator">
      <h1>Our Online Calculator</h1>
      <input class="field field-investment" type="text" placeholder="Regular monthly investment">
      <p class="length-label">Length of investment</p>
      <div class="slider"><div class="slider-fill"></div><div class="slider-thumb"></div></div>
      <div class="slider-scale"><span>0</span><span>30 years</span></div>
      <input class="field field-payout" type="text" placeholder="One time payout">
      <p class="or">OR</p>
      <input class="field field-monthly" type="text" placeholder="Monthly Payment">
      <a class="btn-invest" href="#">I WANT TO INVEST</a>
    </section>
  </main>

  <footer class="site-footer">
    <a href="#">ABOUT US</a><span>|</span>
    <a href="#">FAQ</a><span>|</span>
    <a href="#">PRIVACY POLICY</a><span>|</span>
    <a href="#">CONTACT US</a>
  </footer>
</body>
</html>
```